Window Signage to Attract Customers

We need someone to design several window signs for our retail business. These sign graphics will be printed on window cling or vinyl window decal material and ultimately attached to our store windows. The style of the signs should be consistent (please see word document for sign copy). The rough size of these window signs will be approximately 4ft x 3ft and may be reduced to 3ft x 2ft (poster size) so graphics should allow for that. I have attached an example of a competitor's signs. I have also attached our logo and other signs we have to use as examples of our colors and for style inspiration.
Target Market(s)
Drive and walk by consumers

```html
<!DOCTYPE html>
<html lang="en">
<head>
<meta charset="utf-8">
<title>Checks Cashed – Window Sign</title>
<link rel="stylesheet" href="https://fonts.googleapis.com/css2?family=Anton&family=Oswald:wght@600&display=swap">
<style>
  :root {
    --sign-pink: #ff0a5c;
    --sign-yellow: #fff000;
    --sign-gold: #dba400;
    --sign-ink: #333333;
    --sign-shadow: rgba(0, 0, 0, 0.28);
    --sign-white: #ffffff;
  }
  html, body {
    margin: 0;
    padding: 0;
    overflow: hidden;
    background: var(--sign-white);
  }
  .window-sign {
    display: block;
    width: 1200px;
    height: 1200px;
  }
  .headline {
    font-family: "Anton", "Oswald", sans-serif;
    stroke: var(--sign-ink);
    stroke-linejoin: round;
    paint-order: stroke fill;
  }
  .headline--initial { stroke-width: 22px; }
  .headline--line { stroke-width: 14px; }
  .banner-text {
    font-family: "Anton", "Oswald", sans-serif;
    fill: var(--sign-pink);
    stroke: var(--sign-ink);
    stroke-width: 6px;
    stroke-linejoin: round;
    paint-order: stroke fill;
  }
  .brand-name {
    font-family: "Anton", "Oswald", sans-serif;
    fill: var(--sign-pink);
  }
  .disclaimer {
    font-family: "Oswald", sans-serif;
    font-weight: 600;
    font-size: 15px;
    fill: var(--sign-white);
  }
</style>
</head>
<body>
<svg class="window-sign" viewBox="0 0 1200 1200" xmlns="http://www.w3.org/2000/svg">
  <defs>
    <linearGradient id="tone-initial" gradientUnits="userSpaceOnUse" x1="0" y1="0" x2="0" y2="1200">
      <stop offset="0.34" stop-color="var(--sign-gold)"/>
      <stop offset="0.34" stop-color="var(--sign-yellow)"/>
    </linearGradient>
    <linearGradient id="tone-checks" gradientUnits="userSpaceOnUse" x1="0" y1="0" x2="0" y2="1200">
      <stop offset="0.2767" stop-color="var(--sign-gold)"/>
      <stop offset="0.2767" stop-color="var(--sign-yellow)"/>
    </linearGradient>
    <linearGradient id="tone-cashed" gradientUnits="userSpaceOnUse" x1="0" y1="0" x2="0" y2="1200">
      <stop offset="0.4033" stop-color="var(--sign-gold)"/>
      <stop offset="0.4033" stop-color="var(--sign-yellow)"/>
    </linearGradient>
  </defs>

  <!-- main panel -->
  <g class="sign-panel">
    <polygon points="300,164 900,130 900,1052 300,988" fill="var(--sign-shadow)"/>
    <polygon points="312,152 888,120 888,1040 312,976" fill="var(--sign-pink)" stroke="var(--sign-ink)" stroke-width="16" stroke-linejoin="round"/>
  </g>

  <!-- brand pill -->
  <g class="brand-pill">
    <rect x="548" y="58" width="416" height="142" rx="71" fill="var(--sign-shadow)"/>
    <rect x="552" y="54" width="408" height="142" rx="71" fill="var(--sign-ink)"/>
    <rect x="562" y="64" width="388" height="122" rx="61" fill="var(--sign-pink)"/>
    <rect x="572" y="74" width="368" height="102" rx="51" fill="var(--sign-white)"/>
    <circle cx="640" cy="124" r="20" fill="var(--sign-pink)"/>
    <text class="brand-name" x="674" y="138" font-size="54" textLength="214" lengthAdjust="spacingAndGlyphs">CASHWELL</text>
    <text class="brand-name" x="674" y="163" font-size="17" letter-spacing="4" textLength="214" lengthAdjust="spacing">MONEY CENTERS</text>
  </g>

  <!-- headline -->
  <g class="headline-group">
    <text class="headline headline--initial" x="276" y="608" font-size="465" textLength="238" lengthAdjust="spacingAndGlyphs" fill="url(#tone-initial)">C</text>
    <text class="headline headline--line" x="514" y="400" font-size="196" textLength="428" lengthAdjust="spacingAndGlyphs" fill="url(#tone-checks)">HECKS</text>
    <text class="headline headline--line" x="514" y="564" font-size="182" textLength="422" lengthAdjust="spacingAndGlyphs" fill="url(#tone-cashed)">ASHED</text>
  </g>

  <!-- cash icon area -->
  <g class="cash-icon" role="img" aria-label="Icon of a stack of banknotes coming out of a cash slot">
    <rect x="554" y="580" width="306" height="128" rx="14" fill="var(--sign-yellow)" stroke="var(--sign-ink)" stroke-width="12"/>
  </g>

  <!-- service banner -->
  <g class="service-banner">
    <polygon points="232,752 1104,724 1104,900 232,872" fill="var(--sign-shadow)"/>
    <polygon points="244,744 1096,716 1096,892 244,864" fill="var(--sign-yellow)" stroke="var(--sign-ink)" stroke-width="16" stroke-linejoin="round"/>
    <text class="banner-text" x="360" y="836" font-size="80" textLength="684" lengthAdjust="spacingAndGlyphs">PERSONAL &amp; COMMERCIAL</text>
  </g>

  <!-- disclaimer -->
  <g class="disclaimer-block" text-anchor="middle">
    <text class="disclaimer" x="604" y="906">*Approval depends on meeting legal and underwriting requirements.</text>
    <text class="disclaimer" x="604" y="925">All product and service options are subject to change without notice.</text>
    <text class="disclaimer" x="604" y="944">See store for details.</text>
  </g>
</svg>
</body>
</html>
```